Web Design Project - Homepage mockup for media services company

Client would like a site much like this example below in terms of design and layout:

http://fernquill.net/

It's a media services company and the services they provide are:
-audio/video production
-graphic design
-social media
-web development
-apparel design

Their logo file is attached. I have also attached some of their service descriptions if that at all helps with things.

```html
<!DOCTYPE html>
<html lang="en">
<head>
<meta charset="utf-8">
<title>Velmora — Media Services</title>
<link href="https://fonts.googleapis.com/css2?family=Carlito:ital,wght@0,400;0,700;1,700&family=Handlee&display=swap" rel="stylesheet">
<style>
:root{
  --ink-darker:#1e1e1e;
  --nav-bar:#3a3a3a;
  --rule:#5a5a5a;
  --white:#ffffff;
  --text:#4a4a4a;
  --muted:#bdbdbd;
  --brown:#3a1a15;
  --orange-top:#f07a2c;
  --orange-bottom:#c2440e;
  --teal:#1a9aa0;
  --band:#ececec;
  --band-rule:#cfcfcf;
}
*{margin:0;padding:0;box-sizing:border-box}
html,body{width:962px;height:1200px;overflow:hidden}
body{position:relative;font-family:"Carlito",sans-serif;color:var(--text);background:var(--white)}
.abs{position:absolute}

/* header */
.topbar{left:0;top:0;width:962px;height:72px;background:var(--ink-darker)}
.navbar{left:0;top:72px;width:962px;height:40px;background:var(--nav-bar);border-top:1px solid var(--rule);border-bottom:1px solid var(--rule)}
.nav a{position:absolute;top:83px;color:var(--white);font-size:15px;text-decoration:none}
.brand{left:362px;top:4px;width:236px;height:112px}
.brand-dot{position:absolute;left:0;top:0;width:112px;height:112px;border-radius:50%;background:var(--ink-darker);border:4px solid var(--white)}
.brand-name{position:absolute;left:118px;top:38px;font-size:34px;font-weight:700;color:var(--white)}

/* hero */
.hero{left:0;top:112px;width:962px;height:341px;background:linear-gradient(180deg,#2e2e2e,#232323)}
.hero-title{left:97px;top:198px;font-family:"Handlee",cursive;font-weight:400;font-size:25px;color:var(--white)}
.hero-text{left:97px;top:244px;width:322px;font-size:14.5px;line-height:17.4px;letter-spacing:.3px;color:var(--white);text-align:justify}
.btn{display:flex;align-items:center;justify-content:center;color:var(--white);font-weight:700;border-radius:18px;background:linear-gradient(180deg,var(--orange-top),var(--orange-bottom));border:1px solid #8c3208;text-shadow:0 1px 1px rgba(0,0,0,.45)}
.btn-learn{left:97px;top:363px;width:197px;height:33px;font-size:18px}
.hero-media{left:500px;top:129px;width:343px;height:324px;background:linear-gradient(160deg,#cfcfcf,#f2f2f2 45%,#b8b8b8)}

/* services */
.service{top:476px;width:180px;text-align:center}
.service-icon{display:block;margin:0 auto;width:54px;height:54px}
.service h3{font-family:"Handlee",cursive;font-weight:400;font-size:19px;color:var(--brown);margin-top:6px}
.service p{font-size:11px;line-height:13.6px;margin-top:6px;color:#555}

/* quote band */
.band{left:0;top:660px;width:962px;height:59px;background:var(--band);border-top:1px solid var(--band-rule);border-bottom:1px solid var(--band-rule)}
.band-text{left:100px;top:671px;width:540px;text-align:center;font-size:16px;font-weight:700;font-style:italic;line-height:16.5px;color:#2a2a2a}
.band-text em{color:var(--teal)}
.btn-quote{left:668px;top:674px;width:197px;height:31px;font-size:17px}

/* about */
.about-title{left:97px;top:744px;font-family:"Handlee",cursive;font-weight:400;font-size:24px;color:var(--brown)}
.about-text{left:97px;top:783px;width:421px;font-size:11px;line-height:13.7px;letter-spacing:.1px;text-align:justify;color:#555}
.about-text p+p{margin-top:13px}
.about-media{left:553px;top:752px;width:318px;height:177px;background:linear-gradient(180deg,#3a3a3a,#c9ced4 30%,#f2f2f2 70%,#cfcfcf)}

/* footer */
.footer{left:0;top:962px;width:962px;height:238px;background:linear-gradient(180deg,#282828,#1f1f1f)}
.foot-col{top:980px;color:var(--muted);font-size:11px}
.foot-col h4{font-family:"Handlee",cursive;font-weight:400;font-size:16px;color:var(--white);margin-bottom:20px}
.foot-col li{list-style:none;height:19.3px}
.tweet,.contact-row{display:flex;gap:8px;margin-bottom:12px;line-height:13.7px}
.tweet strong{font-weight:400;color:var(--white)}
.ico{flex:none;width:11px;height:11px;margin-top:2px}
.foot-rule{left:97px;top:1158px;width:768px;height:1px;background:#474747}
.copyright{left:97px;top:1170px;font-size:11px;color:var(--muted)}
.social{top:1166px;width:19px;height:19px;background:#5c5c5c;border-radius:2px}
</style>
</head>
<body>

<header>
  <div class="abs topbar"></div>
  <div class="abs navbar"></div>
  <nav class="nav">
    <a style="left:117px">Home</a>
    <a style="left:185px">About us</a>
    <a style="left:270px">Portfolio</a>
    <a style="left:643px">Services</a>
    <a style="left:724px">Blog</a>
    <a style="left:782px">Contact us</a>
  </nav>
  <div class="abs brand">
    <span class="brand-dot"></span>
    <span class="brand-name">Velmora</span>
  </div>
</header>

<section>
  <div class="abs hero"></div>
  <h1 class="abs hero-title">Lorem ipsum dolor sit</h1>
  <p class="abs hero-text">Lorem ipsum dolor sit amet, consectetur adipiscing elit. Fusce vitae justo urna, in commodo lectus. Duis augue erat, interdum vel interdum quis, rutrum in augue. Suspendisse suscipit placerat enim eu volutpat.</p>
  <a class="abs btn btn-learn">Learn More</a>
  <div class="abs hero-media" role="img" aria-label="Photo of a desktop monitor displaying a portfolio website"></div>
</section>

<section>
  <div class="abs service" style="left:94px">
    <svg class="service-icon" viewBox="0 0 54 54"><circle cx="27" cy="27" r="27" fill="var(--brown)"/><ellipse cx="28" cy="24" rx="15" ry="10" fill="#fff"/><circle cx="17" cy="36" r="3" fill="#fff"/><circle cx="13" cy="41" r="2" fill="#fff"/></svg>
    <h3>Social Media</h3>
    <p>Duis mollis, est non commodo luctus, nisi erat porttitor ligula, eget lacinia odio sem nec elit. Duis mollis, est non commodo luctus, nisi ligula.</p>
  </div>
  <div class="abs service" style="left:292px">
    <svg class="service-icon" viewBox="0 0 54 54"><circle cx="27" cy="27" r="27" fill="var(--brown)"/><g fill="#fff"><rect x="14" y="22" width="3" height="14"/><rect x="19" y="17" width="3" height="19"/><rect x="24" y="14" width="3" height="22"/><rect x="29" y="19" width="3" height="17"/><rect x="34" y="16" width="3" height="20"/><rect x="39" y="24" width="3" height="12"/></g></svg>
    <h3>Audio Production</h3>
    <p>Duis mollis, est non commodo luctus, nisi erat porttitor ligula, eget lacinia odio sem nec elit. Duis mollis, est non commodo luctus, nisi ligula.</p>
  </div>
  <div class="abs service" style="left:490px">
    <svg class="service-icon" viewBox="0 0 54 54"><circle cx="27" cy="27" r="27" fill="var(--brown)"/><rect x="14" y="15" width="26" height="18" rx="1" fill="#fff"/><rect x="17" y="18" width="20" height="12" fill="var(--brown)"/><rect x="24" y="33" width="6" height="4" fill="#fff"/><rect x="19" y="37" width="16" height="2" fill="#fff"/></svg>
    <h3>Website Design</h3>
    <p>Duis mollis, est non commodo luctus, nisi erat porttitor ligula, eget lacinia odio sem nec elit. Duis mollis, est non commodo luctus, nisi ligula.</p>
  </div>
  <div class="abs service" style="left:687px">
    <svg class="service-icon" viewBox="0 0 54 54"><circle cx="27" cy="27" r="27" fill="var(--brown)"/><rect x="12" y="18" width="30" height="20" rx="3" fill="#fff"/><rect x="21" y="14" width="12" height="5" rx="1" fill="#fff"/><circle cx="27" cy="28" r="7" fill="var(--brown)"/><circle cx="27" cy="28" r="4" fill="#fff"/></svg>
    <h3>Photography</h3>
    <p>Duis mollis, est non commodo luctus, nisi erat porttitor ligula, eget lacinia odio sem nec elit. Duis mollis, est non commodo luctus, nisi ligula.</p>
  </div>
</section>

<section>
  <div class="abs band"></div>
  <p class="abs band-text">Aliquam tincidunt feugiat hendrerit. Proin sit amet mi neque,<br>a sollicitudin est. Maecenas <em>pulvinar tellus</em> et neque tristique molestie.</p>
  <a class="abs btn btn-quote">Request A Quote</a>
</section>

<section>
  <h2 class="abs about-title">About Us</h2>
  <div class="abs about-text">
    <p>Lorem ipsum dolor sit amet, consectetur adipiscing elit. Fusce lectus nibh, semper eget vulputate vel, consequat sed ipsum. Aenean a suscipit dui. Maecenas porta, mi ac aliquam fermentum, libero justo dapibus lectus, non pellentesque massa nunc vel mauris. Ut ornare dapibus blandit. Ut blandit, ante in pellentesque tempor, lacus mauris cursus dui, id pellentesque odio erat ac justo. Nullam laoreet turpis elit, in vulputate erat. Curabitur urna lacus, fringilla id sagittis.</p>
    <p>in, tincidunt ac turpis. Nullam at quam dictum orci vulputate rutrum. Nulla convallis augue vitae tortor convallis nec aliquam eros tempus. Suspendisse sit amet sollicitudin erat. Nam rutrum, eros a feugiat ultrices.</p>
  </div>
  <div class="abs about-media" role="img" aria-label="Photo of a laptop displaying a business website"></div>
</section>

<footer>
  <div class="abs footer"></div>
  <div class="abs foot-col" style="left:97px">
    <h4>Navigation</h4>
    <ul><li>Home</li><li>About us</li><li>Portfolio</li><li>Services</li><li>Blog</li><li>Contact us</li></ul>
  </div>
  <div class="abs foot-col" style="left:275px">
    <h4>Services</h4>
    <ul><li>Audio / Video Production</li><li>Graphic Design</li><li>Social Media</li><li>Web Development</li><li>Apparel Design</li><li>Photography</li></ul>
  </div>
  <div class="abs foot-col" style="left:472px;width:190px">
    <h4>Recent Tweets</h4>
    <div class="tweet"><svg class="ico" viewBox="0 0 11 11"><circle cx="5.5" cy="5.5" r="5" fill="#8a8a8a"/></svg><span>Lorem ipsum dolor sit amet, consectetur adipiscing elit.<br><strong>about 2 hours ago</strong></span></div>
    <div class="tweet"><svg class="ico" viewBox="0 0 11 11"><circle cx="5.5" cy="5.5" r="5" fill="#8a8a8a"/></svg><span>Lorem ipsum dolor sit amet, consectetur adipiscing elit.<br><strong>about 2 hours ago</strong></span></div>
  </div>
  <div class="abs foot-col" style="left:689px;width:180px">
    <h4>Contact us</h4>
    <div class="contact-row"><svg class="ico" viewBox="0 0 11 11"><path d="M5.5 0.5a3.5 3.5 0 0 1 3.5 3.5c0 2.5-3.5 6.5-3.5 6.5S2 6.5 2 4a3.5 3.5 0 0 1 3.5-3.5z" fill="#9a9a9a"/><circle cx="5.5" cy="4" r="1.3" fill="#262626"/></svg><span>Lorem ipsum dolor sit amet, adipiscing elit.</span></div>
    <div class="contact-row"><svg class="ico" viewBox="0 0 11 11"><path d="M2 1 L4 1 L5 3.5 L3.8 4.5 Q5 7 6.5 7.2 L7.5 6 L10 7 L10 9 Q9 10.5 7 10 Q2 8 1 3 Q0.8 1.5 2 1Z" fill="#9a9a9a"/></svg><span>+1 555 0142</span></div>
    <div class="contact-row"><svg class="ico" viewBox="0 0 11 11"><rect x="1" y="2" width="9" height="7" fill="#9a9a9a"/><path d="M1 2 L5.5 6 L10 2" stroke="#262626" fill="none"/></svg><span>info@velmoramedia.net</span></div>
  </div>
  <div class="abs foot-rule"></div>
  <p class="abs copyright">Copyright © 2012 Velmora. All Right Reserved.</p>
  <span class="abs social" style="left:776px"></span>
  <span class="abs social" style="left:807px"></span>
  <span class="abs social" style="left:838px"></span>
</footer>

</body>
</html>
```